High end building company who specialise in architecturally designed homes needing a presentation do

We need a document/template that can be used in Indesign. We present proposal's, house plans, specifications at various stages throughout a building project from initial contact right through to completion. We want to have the same feel through out each presentation and be able to use the same first few pages and then be able to insert the contents. Sometimes the content will be A4 and other times when presenting plans will be A3. I have attached an example of one previously used for presenting plans (see 01_Conceptual) and one for proposals (see Proposal Example ). The document needs to have a minimalist look and feel very sophisticated to suit our client base. The look of the document should tie in with our logo design which is also attached.

```html
<!DOCTYPE html>
<html lang="en">
<head>
<meta charset="utf-8">
<title>Vandermeer Residence — Concept Design</title>
<link rel="stylesheet" href="https://fonts.googleapis.com/css2?family=Montserrat:wght@200;400&display=swap">
<style>
  :root {
    --backdrop: #464445;
    --ink: #2b2a2b;
    --accent: #e8541e;
    --veil: rgba(255, 255, 255, 0.55);
    --photo-light: #e4e4e4;
    --photo-mid: #b9b9b9;
    --photo-dark: #7d7d7d;
  }
  * { margin: 0; padding: 0; box-sizing: border-box; }
  html, body {
    width: 1200px; height: 1200px; overflow: hidden;
    background: var(--backdrop);
  }
  .cover {
    position: absolute; left: 62px; top: 200px;
    width: 1080px; height: 764px; overflow: hidden;
  }
  .cover-photo {
    position: absolute; inset: 0;
    background:
      linear-gradient(180deg, var(--photo-mid) 0%, var(--photo-light) 30%, var(--photo-light) 62%, var(--photo-mid) 100%),
      var(--photo-light);
  }
  .cover-photo::after {
    content: ""; position: absolute; inset: 0;
    background: linear-gradient(90deg, rgba(125,125,125,0.35) 0%, rgba(255,255,255,0) 18%, rgba(255,255,255,0) 90%, rgba(80,80,80,0.35) 100%);
  }
  .title-veil {
    position: absolute; left: 64px; top: 64px;
    width: 952px; height: 636px;
    background: var(--veil);
  }
  .slash {
    position: absolute; inset: 0; width: 1080px; height: 764px;
  }
  .title-block {
    position: absolute; right: 100px; top: 98px; text-align: right;
    font-family: "Montserrat", sans-serif;
  }
  .project-name {
    font-weight: 200; font-size: 56px; line-height: 64px;
    color: var(--accent); letter-spacing: 0.2px;
  }
  .stage {
    font-weight: 400; font-size: 32px; line-height: 40px;
    color: var(--ink); margin-top: 2px;
  }
  .issue-date {
    font-weight: 400; font-size: 20px; line-height: 26px;
    color: var(--ink); margin-top: 2px;
  }
  .company {
    position: absolute; left: 81px; top: 595px;
    display: flex; align-items: center; gap: 18px;
  }
  .company-dot {
    width: 86px; height: 86px; border-radius: 50%;
    background: var(--ink);
  }
  .company-name {
    font-family: "Montserrat", sans-serif; font-weight: 400;
    font-size: 18px; line-height: 24px;
    color: var(--ink); white-space: nowrap;
  }
</style>
</head>
<body>
  <section class="cover">
    <div class="cover-photo" role="img" aria-label="Black and white photograph of a modern home exterior with vertical timber battens framing a glazed upper level"></div>
    <div class="title-veil"></div>
    <svg class="slash" viewBox="0 0 1080 764" aria-hidden="true">
      <line x1="224" y1="64" x2="520" y2="700" stroke="var(--ink)" stroke-width="3"/>
    </svg>
    <header class="title-block">
      <h1 class="project-name">Vandermeer Residence</h1>
      <p class="stage">CONCEPT DESIGN</p>
      <p class="issue-date">10 September 2015</p>
    </header>
    <div class="company">
      <div class="company-dot"></div>
      <p class="company-name">Harlow Reid Constructions</p>
    </div>
  </section>
</body>
</html>
```